Letterhead Design

We need a new Letterhead design for a 30 year old Electrical Company. We service domestic and commercial places. We have a logo recently made so to incorporate that. Using same colours or interested to see others added.
Would like to see a couple of options with all the info in letterhead, then another with info in a footnote down the bottom.

info needed to be added:

-Lic. No 48162
8/22-24 Larkin Rd, Tolvern 2087
W - brightcoilpower.com.au
T - (02) 9471 3825
M - 0427 593 168
E - info@brightcoilpower.com.au
ABN: 42 597 214 630

Electrical

```html
<!DOCTYPE html>
<html lang="en">
<head>
<meta charset="utf-8">
<title>Brightcoil Power Electrical – Letterhead</title>
<link rel="stylesheet" href="https://fonts.googleapis.com/css2?family=Arimo:wght@400;700&display=swap">
<style>
  :root {
    --backdrop: #5a5053;
    --paper: #ffffff;
    --brand-teal: #1f4b46;
    --accent-orange: #e9a23b;
    --text-grey: #4a4a4a;
    --watermark-grey: #e3e3e3;
  }
  * { margin: 0; padding: 0; box-sizing: border-box; }
  html, body {
    width: 1200px;
    height: 988px;
    overflow: hidden;
    background: var(--backdrop);
    font-family: "Arimo", Arial, sans-serif;
  }
  .letterhead {
    position: absolute;
    left: 280px;
    top: 41px;
    width: 640px;
    height: 905px;
    background: var(--paper);
    overflow: hidden;
    box-shadow: 0 18px 40px rgba(0,0,0,0.35);
  }
  .brand {
    position: absolute;
    left: 46px;
    top: 44px;
    display: flex;
    align-items: center;
    gap: 10px;
  }
  .brand-dot {
    width: 14px;
    height: 14px;
    border-radius: 50%;
    background: var(--accent-orange);
    flex: none;
  }
  .brand-name {
    font-weight: 700;
    font-size: 22px;
    letter-spacing: 0.5px;
    color: var(--brand-teal);
    white-space: nowrap;
  }
  .brand-rule {
    position: absolute;
    left: 46px;
    top: 80px;
    width: 200px;
    height: 1px;
    background: var(--accent-orange);
  }
  .registration {
    position: absolute;
    left: 46px;
    top: 90px;
    font-size: 10px;
    color: var(--text-grey);
    letter-spacing: 0.3px;
    white-space: nowrap;
  }
  .registration .label {
    color: var(--accent-orange);
    font-weight: 700;
  }
  .watermark {
    position: absolute;
    left: 40px;
    top: 860px;
    transform: rotate(-90deg);
    transform-origin: left top;
    white-space: nowrap;
    font-weight: 400;
    font-size: 30px;
    color: var(--watermark-grey);
    letter-spacing: 1px;
    line-height: 1;
  }
  .watermark-rule {
    position: absolute;
    left: 82px;
    top: 440px;
    width: 1px;
    height: 420px;
    background: var(--watermark-grey);
  }
  .footer {
    position: absolute;
    left: 330px;
    bottom: 40px;
    width: 210px;
  }
  .contact-list {
    list-style: none;
    font-size: 10px;
    color: var(--text-grey);
    line-height: 15px;
  }
  .contact-list li {
    display: flex;
    align-items: center;
    gap: 6px;
    white-space: nowrap;
  }
  .contact-icon {
    width: 10px;
    height: 10px;
    flex: none;
  }
  .footer-rule {
    margin: 6px 0 5px;
    height: 1px;
    background: var(--accent-orange);
  }
  .address {
    font-size: 10px;
    color: var(--text-grey);
    white-space: nowrap;
  }
</style>
</head>
<body>
  <main class="letterhead">
    <div class="watermark" aria-hidden="true">Brightcoil Power Electrical</div>
    <div class="watermark-rule" aria-hidden="true"></div>

    <header>
      <div class="brand">
        <span class="brand-dot"></span>
        <span class="brand-name">Brightcoil Power Electrical</span>
      </div>
      <div class="brand-rule"></div>
      <p class="registration"><span class="label">Lic. No</span> 48162 | <span class="label">ABN:</span> 42 597 214 630</p>
    </header>

    <footer class="footer">
      <ul class="contact-list">
        <li>
          <svg class="contact-icon" viewBox="0 0 10 10" fill="var(--accent-orange)"><path d="M1 3 Q1 1 3 1 L7 1 Q9 1 9 3 L8 4 L6.5 3 L3.5 3 L2 4 Z M2 5 L8 5 L8.5 9 L1.5 9 Z"/></svg>
          (02) 9471 3825
        </li>
        <li>
          <svg class="contact-icon" viewBox="0 0 10 10"><rect x="2.5" y="0.5" width="5" height="9" rx="1" fill="none" stroke="var(--accent-orange)" stroke-width="1"/><circle cx="5" cy="8" r="0.6" fill="var(--accent-orange)"/></svg>
          0427 593 168
        </li>
        <li>
          <svg class="contact-icon" viewBox="0 0 10 10"><rect x="0.5" y="2" width="9" height="6" fill="var(--accent-orange)"/><path d="M0.5 2 L5 5.5 L9.5 2" fill="none" stroke="#fff" stroke-width="0.8"/></svg>
          info@brightcoilpower.com.au
        </li>
        <li>
          <svg class="contact-icon" viewBox="0 0 10 10" fill="none" stroke="var(--accent-orange)" stroke-width="0.9"><circle cx="5" cy="5" r="4.2"/><ellipse cx="5" cy="5" rx="1.8" ry="4.2"/><path d="M0.8 5 H9.2"/></svg>
          www.brightcoilpower.com.au
        </li>
      </ul>
      <div class="footer-rule"></div>
      <p class="address">8/22-24 Larkin Rd, Tolvern 2087</p>
    </footer>
  </main>
</body>
</html>
```